Lantern Signs Facebook Banner Design

Design a facebook banner for a sign company. I would like to have a modern approach to it.

Product Offering:
Signs
Banners
Decals
Commercial Wraps

```html
<!DOCTYPE html>
<html lang="en">
<head>
<meta charset="utf-8">
<title>Lantern Signs — Facebook Banner</title>
<link rel="stylesheet" href="https://fonts.googleapis.com/css2?family=Open+Sans:wdth,wght@75,700;75,800&display=swap">
<style>
  :root {
    --red-deep: #6e0000;
    --red-main: #a10303;
    --red-bright: #b80a0a;
    --wave-dark: rgba(70, 0, 0, 0.45);
    --wave-light: rgba(190, 20, 20, 0.35);
    --white: #ffffff;
  }
  html, body {
    margin: 0;
    padding: 0;
    overflow: hidden;
    background: var(--red-deep);
  }
  .banner {
    position: relative;
    width: 1200px;
    height: 527px;
    overflow: hidden;
    background: radial-gradient(ellipse at 45% 45%, var(--red-bright) 0%, var(--red-main) 45%, var(--red-deep) 100%);
    font-family: "Open Sans", Arial, sans-serif;
    font-stretch: 75%;
    color: var(--white);
  }
  .banner__waves {
    position: absolute;
    inset: 0;
    width: 100%;
    height: 100%;
  }
  .brand {
    position: absolute;
    left: 0;
    right: 0;
    top: 118px;
    margin: 0;
    text-align: center;
    font-weight: 800;
    color: var(--white);
    text-transform: uppercase;
    line-height: 0.9;
  }
  .brand__line--main {
    display: block;
    font-size: 220px;
    letter-spacing: 6px;
  }
  .brand__line--sub {
    display: block;
    font-size: 120px;
    letter-spacing: 4px;
    margin-top: 4px;
  }
  .services {
    position: absolute;
    left: 0;
    right: 0;
    top: 458px;
    margin: 0;
    padding: 0;
    list-style: none;
    display: flex;
    justify-content: center;
    gap: 14px;
    font-weight: 700;
    font-size: 34px;
    letter-spacing: 0.5px;
    text-transform: uppercase;
  }
  .services__item + .services__item::before {
    content: "•";
    margin-right: 14px;
  }
</style>
</head>
<body>
  <main class="banner">
    <svg class="banner__waves" viewBox="0 0 1200 527" preserveAspectRatio="none" aria-hidden="true">
      <path d="M0 0 H1200 V90 C1000 40 760 20 520 70 C320 110 150 60 0 20 Z" fill="var(--wave-dark)"/>
      <path d="M0 527 V380 C180 430 360 470 560 440 C800 400 1000 330 1200 360 V527 Z" fill="var(--wave-dark)"/>
      <path d="M820 0 C900 120 1060 180 1200 170 V0 Z" fill="var(--wave-light)"/>
      <path d="M0 180 C90 230 160 320 120 527 H0 Z" fill="var(--wave-light)"/>
      <path d="M1000 527 C1040 420 1120 380 1200 370 V527 Z" fill="var(--wave-dark)"/>
    </svg>

    <h1 class="brand">
      <span class="brand__line brand__line--main">Lantern</span>
      <span class="brand__line brand__line--sub">Signs</span>
    </h1>

    <ul class="services">
      <li class="services__item">Signs</li>
      <li class="services__item">Banners</li>
      <li class="services__item">Decals</li>
      <li class="services__item">Commercial Wraps</li>
    </ul>
  </main>
</body>
</html>
```